LITTLE DESIGN WORK REQUIRED!

UPDATE: WE WEREN'T OVERLY ECSTATIC WITH THE DESIGNS WE WERE RECEIVING SO WE DID MOST OF THE DESIGN WORK OURSELVES...

PLEASE SEE THE NEWLY ATTACHED PPT DOC TO VIEW NEARLY EXACT REPLICAS OF WHAT WE WANT THE SITE TO LOOK LIKE. WE NOW NEED YOUR HELP TO MAKE IT LOOK LIKE SOMETHING WORTHY OF THE WEB.

NO CODING REQUIRED - EXPECTED OUTPUT PSD FILES

Hi everyone!

We're looking for a designer to work their magic for our site! We're a not-for-profit program aimed at helping young people realise their potential!

In the attached PPT file, you'll notice we've already DESIGNED THE ENTIRE SITE IN POWERPOINT. Now, we need YOU to make the small changes we requested in the document as well as design the whole thing in psd.

Any questions, don't hesitate to ask.

Brook-Rise
Updates

We've done about 95% of the design for you. Please fine-tune it. See the newly attached PPT doc for details. 

The best two designs will win. This project closes on Friday - please message us if you are absolutely sure you cannot make the deadline.

Thanks,
Brook-Rise

```html
<!DOCTYPE html>
<html lang="en">
<head>
<meta charset="utf-8">
<title>Brook-Rise</title>
<link href="https://fonts.googleapis.com/css2?family=Open+Sans:ital,wght@0,300;0,400;0,600;0,700;1,300;1,400;1,600;1,700&family=Alfa+Slab+One&display=swap" rel="stylesheet">
<style>
  :root {
    --grass: #6aa31a;
    --lime: #86bd14;
    --lime-bright: #8cc51a;
    --forest: #1f4d16;
    --navy: #2a3f7c;
    --navy-deep: #223468;
    --ink: #1d1d1d;
    --text: #333333;
    --page: #ffffff;
    --footer: #000000;
    --footer-text: #ffffff;
    --discover: #1c6fc0;
    --design: #e06c0e;
    --build: #cc1010;
    --achieve: #7fb616;
    --amber: #d4640c;
    --nav-grey: #d6d6d6;
  }
  * { box-sizing: border-box; margin: 0; padding: 0; }
  html, body { width: 1200px; height: 2362px; overflow: hidden; }
  body {
    position: relative;
    font-family: "Open Sans", Arial, sans-serif;
    color: var(--text);
    background: var(--grass);
  }
  .abs { position: absolute; }

  .page { left: 146px; top: 0; width: 912px; height: 2040px; background: var(--page); }
  .footer { left: 0; top: 2040px; width: 1200px; height: 322px; background: var(--footer); }

  /* header */
  .brand { left: 180px; top: 44px; display: flex; align-items: center; gap: 14px; }
  .brand-mark { width: 44px; height: 44px; border-radius: 50%; background: var(--lime-bright); }
  .brand-name { font-weight: 700; font-size: 42px; color: var(--ink); letter-spacing: -0.5px; }
  .share { left: 898px; top: 89px; width: 113px; height: 38px; background: var(--navy); border: 2px solid #4d66a8; border-radius: 3px;
           color: #fff; font-size: 15px; font-weight: 600; display: flex; align-items: center; justify-content: center; gap: 8px; }
  .share-box { width: 16px; height: 16px; background: #fff; border-radius: 2px; }

  .nav { top: 153px; height: 34px; border-radius: 2px; font-size: 15px; color: #333;
         background: linear-gradient(#ececec, var(--nav-grey)); border: 1px solid #bdbdbd;
         display: flex; align-items: center; justify-content: center; gap: 8px; }
  .nav.active { background: linear-gradient(#9ed42a, #6ea812); color: #fff; border-color: #5f9410; }
  .nav .caret { font-size: 9px; opacity: .7; }

  /* hero + feats */
  .hero { left: 165px; top: 214px; width: 582px; height: 350px;
          background: linear-gradient(180deg, #5c7a2a 0%, #a78a3a 45%, #d7a334 75%, #c48a2c 100%); }
  .feats { left: 765px; top: 214px; width: 270px; height: 350px;
           background: radial-gradient(circle at 50% 50%, #2e6a20, var(--forest)); color: #fff; text-align: center; }
  .feats-rule { position: absolute; left: 28px; right: 28px; height: 3px; background: #fff; }
  .feats-title { position: absolute; top: 84px; width: 100%; font-family: "Alfa Slab One", Georgia, serif; font-size: 50px; letter-spacing: 2px; }
  .feats-copy { position: absolute; top: 158px; width: 100%; font-size: 29px; line-height: 1.2; }

  /* intro */
  .welcome { left: 168px; top: 576px; font-size: 38px; font-style: italic; font-weight: 300; color: var(--ink); }
  .welcome strong { color: var(--lime); font-weight: 700; }
  .intro { left: 170px; width: 570px; font-size: 14.5px; line-height: 22px; color: var(--text); }
  .intro b { color: var(--ink); }
  .section-title { left: 168px; top: 770px; font-size: 38px; font-weight: 400; color: var(--ink); }

  /* category bands */
  .band { left: 166px; width: 575px; height: 41px; border-radius: 3px; color: #fff; font-style: italic;
          font-size: 16px; display: flex; align-items: center; justify-content: space-between; padding: 0 20px 0 14px; }
  .band .help { font-style: normal; font-size: 14px; }
  .band-discover { background: var(--discover); }
  .band-design { background: var(--design); }
  .band-build { background: var(--build); }
  .band-achieve { background: var(--achieve); }

  /* posts */
  .post-image { width: 282px; height: 147px; border: 1px solid #bcbcbc; }
  .post-title { font-size: 24px; color: var(--ink); }
  .post-title b { font-weight: 700; }
  .post-excerpt { font-size: 12.5px; color: var(--text); white-space: nowrap; width: 282px; overflow: hidden; }
  .tone-office { background: linear-gradient(135deg, #e8e4df, #b9b3ab); }
  .tone-leap { background: linear-gradient(180deg, #9c4fa6, #c35bb3 70%, #111 70%); }
  .tone-team { background: linear-gradient(135deg, #dbe6ee, #8fa8bc); }
  .tone-sport { background: linear-gradient(135deg, #7a4a2c, #c9a77a); }
  .tone-crowd { background: linear-gradient(135deg, #b8c3cf, #3d4656); }
  .tone-relax { background: linear-gradient(135deg, #f0f0f0, #5c86b5); }

  /* sidebar */
  .touch { left: 765px; top: 576px; width: 270px; height: 120px; background: var(--navy); color: #fff; }
  .touch-title { position: absolute; top: 18px; width: 100%; text-align: center; font-size: 22px; font-weight: 600; }
  .like { position: absolute; left: 34px; top: 60px; width: 44px; height: 20px; background: #eceef4; border: 1px solid #999;
          border-radius: 2px; color: #333; font-size: 10px; display: flex; align-items: center; justify-content: center; }
  .like-text { position: absolute; left: 94px; top: 58px; width: 150px; font-size: 10px; line-height: 14px; }

  .activity { left: 765px; top: 711px; width: 265px; height: 328px; background: var(--navy-deep); color: #fff; }
  .activity-head { height: 26px; background: #111; display: flex; justify-content: space-between; align-items: center; padding: 0 10px; font-size: 14px; }
  .activity-head b { font-size: 11px; }
  .activity-item { position: absolute; left: 16px; display: flex; gap: 10px; }
  .activity-icon { width: 26px; height: 26px; background: #5a6fa6; border: 1px solid #8c9cc6; }
  .activity-item p { font-size: 9px; line-height: 11px; width: 190px; }
  .activity-foot { position: absolute; left: 10px; right: 10px; bottom: 6px; border-top: 1px solid #44578f; padding-top: 8px; font-size: 8px; }

  .side-label { left: 767px; font-size: 15px; color: var(--ink); }
  .popular { left: 765px; top: 1083px; width: 270px; height: 309px; background: var(--lime); }
  .pop-item { position: absolute; left: 18px; display: flex; gap: 10px; }
  .avatar { width: 44px; height: 44px; border: 2px solid #fff; background: linear-gradient(135deg, #e0b48c, #8a5a38); }
  .pop-item strong { display: block; font-size: 15px; font-weight: 400; color: var(--ink); }
  .pop-item small { font-size: 10px; color: #223; }

  .ambassador { left: 765px; width: 267px; height: 118px; background: var(--amber); }
  .portrait { position: absolute; left: 14px; top: 14px; width: 86px; height: 88px; border: 2px solid #fff; background: linear-gradient(135deg, #d9d9d9, #6e6e6e); }
  .amb-name { position: absolute; left: 108px; top: 14px; font-size: 14px; font-weight: 700; color: var(--ink); }
  .amb-role { position: absolute; left: 108px; top: 36px; font-size: 11px; line-height: 17px; color: #1f1f1f; }
  .meet { position: absolute; left: 108px; top: 80px; padding: 1px 8px; background: var(--lime-bright); border: 1px solid #5e8f0f; font-size: 10px; color: #223; }

  /* footer */
  .foot-col { top: 2078px; width: 220px; text-align: center; color: var(--footer-text); }
  .foot-col h3 { font-size: 18px; font-weight: 400; padding-bottom: 10px; border-bottom: 1px solid #333; }
  .foot-links { list-style: none; margin-top: 10px; font-size: 13px; line-height: 27px; }
  .foot-address { margin-top: 14px; font-size: 13px; line-height: 26px; }
  .social { top: 2126px; width: 48px; height: 48px; border-radius: 9px; }
</style>
</head>
<body>
  <div class="abs page"></div>

  <header>
    <div class="abs brand"><span class="brand-mark"></span><span class="brand-name">BROOK-RISE</span></div>
    <a class="abs share"><span class="share-box"></span>SHARE</a>
    <nav>
      <div class="abs nav active" style="left:192px;width:101px">Home <span class="caret">▼</span></div>
      <div class="abs nav" style="left:333px;width:111px">About Us <span class="caret">▼</span></div>
      <div class="abs nav" style="left:473px;width:112px">Resources <span class="caret">▼</span></div>
      <div class="abs nav" style="left:614px;width:120px">Workshops <span class="caret">▼</span></div>
      <div class="abs nav" style="left:763px;width:132px">Ambassadors <span class="caret">▼</span></div>
      <div class="abs nav" style="left:926px;width:84px">Feats <span class="caret">▼</span></div>
    </nav>
  </header>

  <main>
    <div class="abs hero" role="img" aria-label="Three giraffes walking across golden savanna grass"></div>

    <h1 class="abs welcome">Welcome to <strong>Brook-Rise</strong></h1>
    <p class="abs intro" style="top:638px"><b>Brook-Rise</b> is a not-for-profit program aimed at helping people &nbsp;-- especially young people -- realise their potential and achieve success.</p>
    <p class="abs intro" style="top:704px"><b>Our resources</b> are categorised into four groups : discovery, design, build, and achiever -- the four steps in our achievement framework..</p>

    <h2 class="abs section-title">Recent Posts</h2>

    <div class="abs band band-discover" style="top:833px"><span>Discover</span><span class="help">?</span></div>
    <div class="abs post-image tone-office" style="left:170px;top:891px" role="img" aria-label="Young man working on a laptop in a bright room"></div>
    <div class="abs post-image tone-leap" style="left:459px;top:891px" role="img" aria-label="Silhouette of a person leaping between cliffs against a purple sky"></div>
    <div class="abs post-title" style="left:170px;top:1041px">Title <b>A</b></div>
    <div class="abs post-title" style="left:459px;top:1041px">Title <b>B</b></div>
    <div class="abs post-excerpt" style="left:170px;top:1074px">Lorem ipsum dosectetur adipisicing elit, sed do</div>
    <div class="abs post-excerpt" style="left:459px;top:1074px">Lorem ipsum dosectetur adipisicing elit, sed do</div>

    <div class="abs band band-design" style="top:1119px"><span>Design</span><span class="help">?</span></div>
    <div class="abs post-image tone-team" style="left:170px;top:1183px" role="img" aria-label="Smiling group giving thumbs up"></div>
    <div class="abs post-image tone-sport" style="left:459px;top:1183px" role="img" aria-label="Box of sports balls"></div>
    <div class="abs post-title" style="left:170px;top:1332px">Title <b>C</b></div>
    <div class="abs post-title" style="left:459px;top:1332px">Title <b>D</b></div>
    <div class="abs post-excerpt" style="left:170px;top:1365px">Lorem ipsum dosectetur adipisicing elit, sed do</div>
    <div class="abs post-excerpt" style="left:459px;top:1365px">Lorem ipsum dosectetur adipisicing elit, sed do</div>

    <div class="abs band band-build" style="top:1406px"><span>Build</span><span class="help">?</span></div>
    <div class="abs post-image tone-crowd" style="left:170px;top:1471px" role="img" aria-label="Business team cheering with thumbs up"></div>
    <div class="abs post-image tone-leap" style="left:459px;top:1471px" role="img" aria-label="Silhouette of a person leaping between cliffs against a purple sky"></div>
    <div class="abs post-title" style="left:170px;top:1620px">Title <b>E</b></div>
    <div class="abs post-title" style="left:459px;top:1620px">Title <b>F</b></div>
    <div class="abs post-excerpt" style="left:170px;top:1653px">Lorem ipsum dosectetur adipisicing elit, sed do</div>
    <div class="abs post-excerpt" style="left:459px;top:1653px">Lorem ipsum dosectetur adipisicing elit, sed do</div>

    <div class="abs band band-achieve" style="top:1697px"><span>Achieve</span><span class="help">?</span></div>
    <div class="abs post-image tone-team" style="left:166px;top:1762px" role="img" aria-label="Smiling group giving thumbs up"></div>
    <div class="abs post-image tone-relax" style="left:456px;top:1762px" role="img" aria-label="Young man lying down using a laptop"></div>
    <div class="abs post-title" style="left:166px;top:1910px">Title <b>G</b></div>
    <div class="abs post-title" style="left:456px;top:1910px">Title <b>H</b></div>
    <div class="abs post-excerpt" style="left:166px;top:1943px">Lorem ipsum dosectetur adipisicing elit, sed do</div>
    <div class="abs post-excerpt" style="left:456px;top:1943px">Lorem ipsum dosectetur adipisicing elit, sed do</div>
  </main>

  <aside>
    <div class="abs feats">
      <span class="feats-rule" style="top:78px"></span>
      <div class="feats-title">FEATS</div>
      <span class="feats-rule" style="top:148px"></span>
      <div class="feats-copy">Challenges that<br>dare you to<br>push yourself.</div>
    </div>

    <div class="abs touch">
      <div class="touch-title">Stay In Touch</div>
      <div class="like">Like</div>
      <div class="like-text">22 people like this. Be the first of your friends.</div>
    </div>

    <div class="abs activity">
      <div class="activity-head"><span>Recent Activity</span><b>Friendly</b></div>
      <div class="activity-item" style="top:42px"><span class="activity-icon"></span><p><b>Calling All Entrepreneurship - Come back with Us!</b><br>1,891 people shared this.</p></div>
      <div class="activity-item" style="top:90px"><span class="activity-icon"></span><p><b>Calling All Entrepreneurship - Come back with Us!</b><br>1,891 people shared this.</p></div>
      <div class="activity-item" style="top:138px"><span class="activity-icon"></span><p><b>Calling All Entrepreneurship - Come back with Us!</b><br>1,891 people shared this.</p></div>
      <div class="activity-item" style="top:186px"><span class="activity-icon"></span><p><b>Calling All Entrepreneurship - Come back with Us!</b><br>1,891 people shared this.</p></div>
      <div class="activity-item" style="top:234px"><span class="activity-icon"></span><p><b>Calling All Entrepreneurship - Come back with Us!</b><br>1,891 people shared this.</p></div>
      <div class="activity-foot">friendly</div>
    </div>

    <div class="abs side-label" style="top:1058px">Popular Posts</div>
    <div class="abs popular">
      <div class="pop-item" style="top:20px"><span class="avatar" role="img" aria-label="Member portrait"></span><div><strong>Lorem ipsum dosectetur</strong><small>587 view(s)</small></div></div>
      <div class="pop-item" style="top:76px"><span class="avatar" role="img" aria-label="Member portrait"></span><div><strong>Lorem ipsum dosectetur</strong><small>587 view(s)</small></div></div>
      <div class="pop-item" style="top:132px"><span class="avatar" role="img" aria-label="Member portrait"></span><div><strong>Lorem ipsum dosectetur</strong><small>587 view(s)</small></div></div>
      <div class="pop-item" style="top:188px"><span class="avatar" role="img" aria-label="Member portrait"></span><div><strong>Lorem ipsum dosectetur</strong><small>587 view(s)</small></div></div>
      <div class="pop-item" style="top:244px"><span class="avatar" role="img" aria-label="Member portrait"></span><div><strong>Lorem ipsum dosectetur</strong><small>587 view(s)</small></div></div>
    </div>

    <div class="abs side-label" style="top:1420px">Get To Know Us</div>
    <div class="abs ambassador" style="top:1449px">
      <span class="portrait" role="img" aria-label="Portrait of ambassador Sam Carter"></span>
      <div class="amb-name">Sam Carter</div>
      <div class="amb-role">Young entrepreneur &amp;<br>Brook-Rise Ambassador</div>
      <span class="meet">meet sam</span>
    </div>

    <div class="abs side-label" style="top:1588px">Get To Know Us</div>
    <div class="abs ambassador" style="top:1617px">
      <span class="portrait" role="img" aria-label="Portrait of ambassador Mia Lane"></span>
      <div class="amb-name">Mia Lane</div>
      <div class="amb-role">Professional athlete &amp;<br>Brook-Rise Ambassador</div>
      <span class="meet">meet mia</span>
    </div>
  </aside>

  <footer>
    <div class="abs footer"></div>
    <div class="abs foot-col" style="left:123px">
      <h3>Site Navigation</h3>
      <ul class="foot-links"><li>Home</li><li>About Us</li><li>Resources</li><li>Workshops</li><li>Ambassadors</li><li>Feats</li></ul>
    </div>
    <div class="abs foot-col" style="left:493px"><h3>Follow Us</h3></div>
    <div class="abs social" style="left:500px;background:#3b5fa8" role="img" aria-label="Social profile link"></div>
    <div class="abs social" style="left:557px;background:#3fb0c8" role="img" aria-label="Social profile link"></div>
    <div class="abs social" style="left:614px;background:#e8681e" role="img" aria-label="Social profile link"></div>
    <div class="abs social" style="left:670px;background:#2f7bb5" role="img" aria-label="Social profile link"></div>
    <div class="abs foot-col" style="left:846px">
      <h3>Contact Us</h3>
      <p class="foot-address">48 Fernhill Road, Suite no.9<br>street no.210 near Oak Corner Café<br>Postal code: 4410-BR</p>
    </div>
  </footer>
</body>
</html>
```